Truck Driver Pay - Small Infographic

I need a very small, compact infographic to illustrate the differences in pay for a solo truck driver vs. team truck drivers. This illustration will be viewed on the web exclusively. I have sketched out an idea with all of the content that must be included. I just need a designer's touch.

The attached 'mock up' contains the information to be illustrated/communicated by this infographic.

Target Market(s)

Blue collar employee males ages 18-49 with high school education

Requirements
Must have
• I need 2 versions of the graphic:
• 1) 600 pixels wide for desktop presentation
• 2) 300 pixels wide with vertical scroll for mobile.
• I also require the native .psd or .ai files used to create this infographic.

```html
<!DOCTYPE html>
<html lang="en">
<head>
<meta charset="utf-8">
<title>Understanding Driver Pay</title>
<link href="https://fonts.googleapis.com/css2?family=Bebas+Neue&display=swap" rel="stylesheet">
<style>
  :root {
    --backdrop: #5a1820;
    --paper-light: #fbf0de;
    --paper-dark: #f1d8b6;
    --red: #c9302c;
    --red-dark: #a92622;
    --orange: #e15b31;
    --gold: #f0a42a;
    --teal: #86b8b6;
    --teal-dark: #5f9392;
    --slate: #4f7a7a;
    --green: #3f5b33;
    --olive: #627f4f;
    --cream: #f7e6c8;
    --white: #ffffff;
  }
  * { margin: 0; padding: 0; box-sizing: border-box; }
  html, body { width: 1200px; height: 900px; overflow: hidden; background: var(--backdrop); }
  body { font-family: "Bebas Neue", "Oswald", sans-serif; position: relative; }

  .poster {
    position: absolute; left: 318px; top: 30px; width: 564px; height: 828px;
    background: radial-gradient(ellipse at 50% 45%, var(--paper-light) 0%, var(--paper-dark) 80%);
    box-shadow: 0 6px 18px rgba(0,0,0,.45);
  }
  .poster > * { position: absolute; }

  .title-ribbon { left: 25px; top: 18px; width: 515px; height: 92px; }
  .title-text {
    left: 57px; top: 18px; width: 453px; height: 52px; line-height: 54px;
    text-align: center; color: var(--cream); font-size: 40px; letter-spacing: .5px;
  }

  .truck { top: 100px; width: 88px; height: 120px; background: var(--teal); border-radius: 10px; }
  .truck--solo { left: 22px; }
  .truck--team { left: 460px; }
  .person { top: 145px; width: 30px; height: 76px; background: var(--red); border-radius: 12px 12px 3px 3px; }

  .tag {
    top: 90px; height: 30px; line-height: 32px; padding: 0 10px;
    background: var(--red); color: var(--cream); font-size: 20px; border-radius: 6px;
  }
  .tag::after {
    content: ""; position: absolute; left: 50%; bottom: -8px; margin-left: -8px;
    border: 8px solid transparent; border-bottom: 0; border-top-color: var(--red);
  }

  .divider { left: 280px; top: 92px; width: 3px; height: 678px;
    background: radial-gradient(circle, var(--teal) 1.4px, transparent 1.6px) 0 0 / 3px 9px repeat-y; }

  .paycheck-band { left: 25px; top: 228px; width: 515px; height: 54px; }
  .paycheck-text { left: 47px; top: 230px; width: 470px; height: 38px; line-height: 40px;
    text-align: center; color: var(--white); font-size: 28px; }

  .badge {
    height: 52px; line-height: 52px; text-align: center; color: var(--cream);
    border: 3px solid var(--white); border-radius: 10px; font-size: 27px;
    box-shadow: 0 1px 3px rgba(0,0,0,.25);
  }
  .badge--red { background: var(--red); }
  .badge--green { background: var(--green); }
  .badge::after { content: ""; position: absolute; left: 22px; border: 9px solid transparent; }
  .badge--down::after { bottom: -17px; border-bottom: 0; border-top-color: var(--white); }
  .badge--up::after { top: -17px; border-top: 0; border-bottom-color: var(--white); }
  .badge--big { font-size: 32px; }

  .stat-head { color: var(--slate); font-size: 40px; line-height: 32px; }
  .stat-head sup { font-size: 30px; vertical-align: 6px; }
  .stat-sub { display: block; font-size: 17px; line-height: 16px; }

  .times { width: 32px; height: 28px; line-height: 30px; text-align: center;
    background: var(--green); color: var(--cream); font-size: 19px; }
  .rate { height: 28px; line-height: 30px; padding: 0 8px; background: var(--gold);
    color: var(--white); font-size: 23px; }
  .plan-note { color: var(--gold); font-size: 18px; }
  .pay-label { color: var(--slate); font-size: 29px; line-height: 28px; }
  .pay-label .each { display: block; color: var(--olive); font-size: 24px; }

  .note { padding: 18px 14px 0; font-size: 17px; line-height: 21px; letter-spacing: .2px; }
  .note--red { left: 14px; top: 498px; width: 253px; height: 108px; background: var(--red);
    color: var(--cream); border-radius: 0 30px 30px 0; }
  .note--orange { left: 14px; top: 613px; width: 256px; height: 108px; background: var(--orange);
    color: var(--cream); border-radius: 0 0 0 36px; padding-top: 16px; }
  .note--olive { left: 297px; top: 498px; width: 252px; height: 162px; background: var(--olive);
    color: var(--cream); border-radius: 30px 0 0 0; padding: 14px 8px 0 10px; font-size: 15.5px; line-height: 21.5px; }
  .note--teal { left: 301px; top: 657px; width: 248px; height: 106px; background: var(--teal);
    color: var(--white); border-radius: 34px 0 0 34px; padding: 16px 8px 0 12px; font-size: 16px; line-height: 21px; }

  .footer-band { left: 0; top: 778px; width: 564px; height: 50px; background: var(--red);
    color: var(--cream); text-align: center; font-size: 23px; line-height: 52px; }
</style>
</head>
<body>
<main class="poster">
  <svg class="title-ribbon" viewBox="0 0 515 92" aria-hidden="true">
    <polygon points="0,10 55,10 55,62 0,62 18,36" fill="var(--red-dark)"/>
    <polygon points="515,10 460,10 460,62 515,62 497,36" fill="var(--red-dark)"/>
    <rect x="32" y="0" width="453" height="52" fill="var(--red)"/>
  </svg>
  <h1 class="title-text">Understanding Driver Pay</h1>

  <div class="truck truck--solo" role="img" aria-label="Front view of a semi truck"></div>
  <div class="truck truck--team" role="img" aria-label="Front view of a semi truck"></div>

  <div class="tag" style="left:124px;">1 Truck 1 Driver</div>
  <div class="person" style="left:179px;" role="img" aria-label="Solo driver figure"></div>

  <div class="tag" style="left:298px;">1 Truck 2 Drivers</div>
  <div class="person" style="left:325px;" role="img" aria-label="Team driver figure"></div>
  <div class="person" style="left:385px;" role="img" aria-label="Team driver figure"></div>

  <div class="divider" aria-hidden="true"></div>

  <svg class="paycheck-band" viewBox="0 0 515 54" aria-hidden="true">
    <polygon points="0,16 40,16 40,52 0,52 12,34" fill="var(--teal-dark)"/>
    <polygon points="515,16 475,16 475,52 515,52 503,34" fill="var(--teal-dark)"/>
    <rect x="22" y="2" width="470" height="38" fill="var(--teal)"/>
    <g stroke="var(--white)" stroke-width="1.5" fill="none">
      <path d="M82 15 H150 M82 15 V24 M78 20 L82 25 L86 20"/>
      <path d="M365 15 H433 M433 15 V24 M429 20 L433 25 L437 20"/>
    </g>
  </svg>
  <h2 class="paycheck-text">Example Pay Check</h2>

  <!-- solo column -->
  <div class="badge badge--red badge--down" style="left:57px;top:288px;width:72px;">2500</div>
  <div class="stat-head" style="left:144px;top:290px;">Weekly<sup>*</sup><span class="stat-sub">Miles Driven</span></div>
  <div class="times" style="left:70px;top:365px;">X</div>
  <div class="rate" style="left:102px;top:355px;">.26 Mileage Rate</div>
  <div class="plan-note" style="left:145px;top:393px;">(Classic Plan)</div>
  <div class="badge badge--red badge--up badge--big" style="left:52px;top:425px;width:77px;">$650</div>
  <div class="pay-label" style="left:144px;top:440px;">Weekly Pay</div>

  <!-- team column -->
  <div class="badge badge--green badge--down" style="left:299px;top:288px;width:70px;">4200</div>
  <div class="stat-head" style="left:384px;top:290px;">Weekly<sup>*</sup><span class="stat-sub">Miles Driven</span></div>
  <div class="times" style="left:310px;top:365px;">X</div>
  <div class="rate" style="left:342px;top:355px;">1.75 Mileage Rate</div>
  <div class="badge badge--green badge--up badge--big" style="left:299px;top:425px;width:75px;">$752</div>
  <div class="pay-label" style="left:392px;top:428px;">Weekly Pay<span class="each">(Each Driver)</span></div>

  <p class="note note--red">When a solo driver needs to take his required break, the truck has to stop rolling.</p>
  <p class="note note--orange">Solo drivers can drive a limited amount of miles due to mandates breaks and saftey regulations.</p>
  <p class="note note--olive">Team driver alternate driving duties so the truck can cover more miles. When driver 1 needs to take his required break, driver 2 takes over driving duties until his break is over and they switch places again.</p>
  <p class="note note--teal">The truck keeps rolling and both drivers are paid for the combined miles the truck has been driven.</p>

  <footer class="footer-band">*Weekly mileage will vary. For illustration only</footer>
</main>
</body>
</html>
```